BUSINESS CARD DESIGN

NAME- TODD MASVERIK
PHONE NUMER - 808- 451-7082
EMAIL- OFFICE@VORLINDE-GRADEWAY.COM
BACK OF CARD- SPEACIALIZES IN LAND CLEARING, FORESTRY MUCLHING AND EXCAVATION

Contact Information for Business Card

NAME- TODD MASVERIK PHONE NUMER - 808- 451-7082 EMAIL- OFFICE@VORLINDE-GRADEWAY.COM BACK OF CARD- SPEACIALIZES IN LAND CLEARING , MUCLHING AND EXCAVATION

```html
<!DOCTYPE html>
<html lang="en">
<head>
<meta charset="utf-8">
<title>Business Card – Todd Masverik</title>
<link href="https://fonts.googleapis.com/css2?family=Poppins:wght@400;500;700&display=swap" rel="stylesheet">
<style>
  :root{
    --page:#d6d6d6;
    --black:#050505;
    --carbon:#1c1c1c;
    --green:#5fae12;
    --lime:#b5ea1c;
    --white:#ffffff;
    --mist:#e9e9e9;
    --ink:#111111;
    --rule:#555555;
  }
  html,body{margin:0;padding:0;overflow:hidden}
  body{
    width:686px;height:1200px;background:var(--page);
    display:flex;flex-direction:column;align-items:center;justify-content:center;gap:40px;
    font-family:'Poppins',sans-serif;
  }
  .card{width:600px;height:360px;display:block;box-shadow:0 6px 18px rgba(0,0,0,.25)}
  .fill-black{fill:var(--black)}
  .fill-green{fill:var(--green)}
  .fill-lime{fill:var(--lime)}
  .fill-white{fill:var(--white)}
  .logo-text{font-family:'Poppins',sans-serif;font-size:15px;fill:var(--ink);text-anchor:middle}
  .name{font-family:'Poppins',sans-serif;font-weight:700;font-size:17px;fill:var(--ink);text-anchor:end}
  .name .surname{fill:var(--green)}
  .contact{font-family:'Poppins',sans-serif;font-size:10.5px;fill:var(--ink);text-anchor:end;letter-spacing:.3px}
  .rule{stroke:var(--rule);stroke-width:1.2}
  .tagline{font-family:'Poppins',sans-serif;font-weight:500;font-size:14px;fill:var(--lime);text-anchor:middle;letter-spacing:.3px}
  .web-footer{font-family:'Poppins',sans-serif;font-weight:500;font-size:10px;fill:var(--lime);text-anchor:middle;letter-spacing:.4px}
  .icon-box{fill:var(--green)}
  .icon{fill:var(--white)}
  .icon-line{fill:none;stroke:var(--white);stroke-width:1.2}
</style>
</head>
<body>

<!-- Front of card -->
<svg class="card card-front" viewBox="0 0 555 333" xmlns="http://www.w3.org/2000/svg">
  <defs>
    <radialGradient id="carbonGlow" cx="40%" cy="45%" r="60%">
      <stop offset="0" stop-color="#2a2a2a"/>
      <stop offset="1" stop-color="#050505"/>
    </radialGradient>
    <linearGradient id="siteWash" x1="0" y1="0" x2="0" y2="1">
      <stop offset="0" stop-color="#f7f7f7"/>
      <stop offset="1" stop-color="#dcdcdc"/>
    </linearGradient>
  </defs>
  <rect class="fill-black" width="555" height="333"/>
  <rect width="555" height="333" fill="url(#carbonGlow)"/>
  <polygon class="fill-green" points="0,0 100,0 0,150"/>
  <polygon class="fill-lime" points="345,0 365,0 155,333 135,333"/>
  <polygon points="365,0 555,0 555,333 155,333" fill="url(#siteWash)" role="img" aria-label="Faded photo of an excavator at a land clearing site"/>
  <polygon class="fill-green" points="300,0 370,0 330,65"/>
  <polygon class="fill-green" points="218,232 340,333 155,333"/>
  <polygon class="fill-green" points="555,268 555,333 515,333"/>

  <circle class="fill-lime" cx="128" cy="166" r="52"/>
  <text class="logo-text" x="128" y="160">Logo</text>
  <text class="logo-text" x="128" y="179">Here</text>

  <text class="name" x="513" y="120">TODD <tspan class="surname">MASVERIK</tspan></text>
  <rect class="fill-green" x="488" y="131" width="25" height="3"/>

  <text class="contact" x="485" y="174">808- 451-7082</text>
  <rect class="icon-box" x="497" y="162" width="16" height="16"/>
  <path class="icon" d="M501,166 l2.5,-1 1.5,3 -1.5,1 c1,2 2,3 3.5,3.5 l1,-1.5 3,1.5 -1,2.5 c-5,0 -9,-4 -9,-9z"/>

  <line class="rule" x1="310" y1="191" x2="483" y2="191"/>

  <text class="contact" x="485" y="214">OFFICE@VORLINDE-GRADEWAY.COM</text>
  <rect class="icon-box" x="497" y="202" width="16" height="16"/>
  <rect class="icon" x="500" y="206" width="10" height="8"/>
  <path d="M500,206 l5,4.5 5,-4.5" fill="none" stroke="#5fae12" stroke-width="1"/>

  <line class="rule" x1="310" y1="232" x2="483" y2="232"/>

  <text class="contact" x="485" y="256">VORLINDE-GRADEWAY.COM</text>
  <rect class="icon-box" x="497" y="244" width="16" height="16"/>
  <circle class="icon-line" cx="505" cy="252" r="5"/>
  <ellipse class="icon-line" cx="505" cy="252" rx="2.2" ry="5"/>
  <line class="icon-line" x1="500" y1="252" x2="510" y2="252"/>
</svg>

<!-- Back of card -->
<svg class="card card-back" viewBox="0 0 555 333" xmlns="http://www.w3.org/2000/svg">
  <defs>
    <radialGradient id="carbonGlowBack" cx="50%" cy="30%" r="65%">
      <stop offset="0" stop-color="#262626"/>
      <stop offset="1" stop-color="#030303"/>
    </radialGradient>
    <linearGradient id="jobsite" x1="0" y1="0" x2="0" y2="1">
      <stop offset="0" stop-color="#6fa3d8"/>
      <stop offset=".55" stop-color="#a6a08c"/>
      <stop offset="1" stop-color="#7a5f3e"/>
    </linearGradient>
  </defs>
  <rect class="fill-black" width="555" height="333"/>
  <rect width="555" height="333" fill="url(#carbonGlowBack)"/>
  <polygon class="fill-green" points="0,0 92,0 0,140"/>
  <polygon class="fill-lime" points="98,0 108,0 0,165 0,150"/>
  <polygon class="fill-lime" points="555,135 555,150 438,333 423,333"/>
  <polygon class="fill-green" points="555,158 555,333 443,333"/>

  <circle class="fill-lime" cx="279" cy="72" r="44"/>
  <text class="logo-text" x="279" y="67">Logo</text>
  <text class="logo-text" x="279" y="86">Here</text>

  <text class="tagline" x="278" y="145">SPEACIALIZES IN LAND CLEARING</text>
  <text class="tagline" x="278" y="166">MUCLHING AND EXCAVATION</text>

  <polygon points="112,190 225,190 205,277 92,277" fill="url(#jobsite)" role="img" aria-label="Photo of an excavator digging on a job site"/>
  <polygon points="233,190 345,190 325,277 213,277" fill="url(#jobsite)" role="img" aria-label="Photo of a worker clearing brush"/>
  <polygon points="353,190 462,190 442,277 333,277" fill="url(#jobsite)" role="img" aria-label="Photo of a backhoe loader moving soil"/>

  <text class="web-footer" x="278" y="307">VORLINDE-GRADEWAY.COM</text>
</svg>

</body>
</html>
```